Word template Letterhead for Australian Law Firm

We are a small law firm based in Manly, NSW, Australia. We have had a new logo designed for us and wish to freshen up the appearance of our letterhead. We require the letterhead to be in a word document that we can type over. This will not be a ‘printed’ letterhead because we send the majority of our correspondence via email. We would like to see a few options. We have attached our previous letterhead as well as the artwork for our new logo. We like the idea of a watermark across the bottom of the letter but the watermark must stay in place and we must be able to type over it. We are open to some colour throughout the letterhead because the majority of our correspondence is sent electronically. We also use electronic signatures. I have uploaded an example of this.The letterhead must include:-1. Our address details – including our phone number, physical address, website address etc. These details can be found on the copy of our previous letterhead;2. ABN Number;3. The words ‘Corvenda (NSW) Pty Ltd ACN 742 185 903 trading as Shipton & AssociatesLiability limited by a scheme approved under Professional Standards Legislation. The letterhead does not need to include the names and qualifications of the people working at the firm. Thank you.

Target Market(s)

Clients and other parties

Industry/Entity Type

Law Firm

Font styles to use
Other font styles liked:
• raleway, montserrat

Colors

Designer to choose colors to be used in the design.

Requirements
Must have
• Certain wording - please see project description.
• Must be a word document and must be able to type over the watermark etc.
Nice to have
• Watermark at the bottom of the letter.

```html
<!DOCTYPE html>
<html lang="en">
<head>
<meta charset="utf-8">
<title>Ferrow &amp; Associates Letterhead</title>
<link href="https://fonts.googleapis.com/css2?family=Open+Sans:wght@400;600;700&display=swap" rel="stylesheet">
<style>
  :root {
    --navy: #333f8f;
    --gold: #b9a26a;
    --ink: #2b2b35;
    --muted: #6b6b78;
    --backdrop: #d6dadc;
    --paper: #ffffff;
  }
  * { box-sizing: border-box; margin: 0; padding: 0; }
  html, body { width: 1200px; height: 784px; overflow: hidden; }
  body {
    background: var(--backdrop);
    font-family: "Open Sans", Arial, sans-serif;
    position: relative;
  }
  .letterhead {
    position: absolute;
    left: 337px; top: 20px;
    width: 526px; height: 744px;
    background: var(--paper);
    box-shadow: 0 2px 10px rgba(0,0,0,0.12);
    overflow: hidden;
  }
  .header-accent {
    position: absolute; left: 0; top: 28px;
    width: 26px; height: 8px;
    background: var(--navy);
  }
  .brand {
    position: absolute; left: 40px; top: 22px;
    display: flex; align-items: center; gap: 8px;
  }
  .brand-dot {
    width: 10px; height: 10px; border-radius: 50%;
    background: var(--navy);
  }
  .brand-name {
    font-weight: 600; font-size: 15px; letter-spacing: 0.6px;
    color: var(--ink);
  }
  .header-rule {
    position: absolute; left: 232px; right: 0; top: 46px;
    height: 4px; background: var(--gold);
  }
  .footer {
    position: absolute; left: 0; right: 0; bottom: 0; height: 86px;
  }
  .footer-entity {
    position: absolute; left: 22px; top: 4px;
    font-size: 9.4px; font-weight: 700; color: var(--navy);
    white-space: nowrap;
  }
  .footer-contact {
    position: absolute; left: 22px; top: 22px;
    display: flex; gap: 8px; align-items: center;
    font-size: 7px; color: var(--muted); white-space: nowrap;
  }
  .contact-item { display: flex; align-items: center; gap: 3px; }
  .contact-item svg { width: 7px; height: 7px; fill: var(--ink); }
  .footer-gold {
    position: absolute; left: 0; width: 330px; bottom: 32px;
    height: 4px; background: var(--gold);
  }
  .footer-navy {
    position: absolute; left: 0; width: 100%; bottom: 16px;
    height: 6px; background: var(--navy);
  }
  .footer-web {
    position: absolute; right: 0; bottom: 0;
    width: 210px; height: 28px;
    background: var(--navy);
    clip-path: polygon(18px 0, 100% 0, 100% 100%, 0 100%);
    color: #fff; font-size: 9.5px; font-weight: 600;
    display: flex; align-items: center; justify-content: center;
    padding-left: 14px;
  }
</style>
</head>
<body>
  <main class="letterhead">
    <div class="header-accent"></div>
    <div class="brand">
      <span class="brand-dot"></span>
      <span class="brand-name">Ferrow &amp; Associates</span>
    </div>
    <div class="header-rule"></div>

    <footer class="footer">
      <p class="footer-entity">Corvenda (NSW) Pty Ltd ACN 742 185 903 trading as Ferrow &amp; Associates Liability limited</p>
      <div class="footer-contact">
        <span class="contact-item">
          <svg viewBox="0 0 10 10"><path d="M5 0a3.5 3.5 0 0 0-3.5 3.5C1.5 6 5 10 5 10s3.5-4 3.5-6.5A3.5 3.5 0 0 0 5 0zm0 5a1.5 1.5 0 1 1 0-3 1.5 1.5 0 0 1 0 3z"/></svg>
          Suite 4, 12 Harbour Lane, Seabrook NSW 2101
        </span>
        <span class="contact-item">
          <svg viewBox="0 0 10 10"><circle cx="5" cy="5" r="5"/></svg>
          (02) 9100 4821
        </span>
        <span class="contact-item">
          <svg viewBox="0 0 10 10"><circle cx="5" cy="5" r="5"/></svg>
          (02) 9100 4822
        </span>
        <span class="contact-item">
          <svg viewBox="0 0 10 10"><circle cx="5" cy="5" r="5"/></svg>
          31 742 185 903
        </span>
        <span class="contact-item">
          <svg viewBox="0 0 10 10"><circle cx="5" cy="5" r="5"/></svg>
          reception@corvendalaw.com.au
        </span>
      </div>
      <div class="footer-gold"></div>
      <div class="footer-navy"></div>
      <div class="footer-web">www.ferrowassociates.com.au</div>
    </footer>
  </main>
</body>
</html>
```